Gravel Ale Label design/Graphic design

The Company
Gravel ale is an exciting new brand of ‘fit beer’ targeted at fitness enthusiasts as well as beer lovers. Gravel ale is a craft beer with added protein which can be used as a post work out recovery/leisure beverage. The target audience is generally male, 18-30 years old.
We need label/graphic design of the product to appear on our website www.gravelale-demo.co.uk

The Project
The project is to submit four designs, one for each flavour:
• Larger
• Honey Ale
• Banana Ale
• Zero Alcohol

The design of each flavour must be differentiated, yet have a consistent theme throughout all flavours. At this point Gravel ale has no official logo so feel free to incorporate this into the design, although this is not absolutely necessary.

The label/design should include the following basic information:
Brand name: Gravel Ale
Type: Larger/Honey Ale/Banana Ale/Zero
Tag: 7g High Quality Protein
Alcohol percentage: 4%/Vol (0%/Vol for the Zero alcohol version)
Volume: 300ml

Brand Guidelines (designs not necessarily limited to these)
Font: Aldrich
Main Colours: Blue # 005fbf Orange # ed7000
Basic beer bottle image attached.

The final design will be displayed on (but not limited to) the website www.gravelale-demo.co.uk

The winning designer may be contacted for future projects and opportunities with Gravel Ale.
Updates

Project Deadline Extended
Reason: My apologies I have been sick the last few days and have been unable to provide feedback. Your work is much appreciated, I will extend the project to give us a little more time and provide feedback individually later today. Best Regards, Oliver

Target Market(s)

The target audience is generally male, 18-30 years old.

Industry/Entity Type

Fitness

Requirements
Must have
• The label/design should include the following basic information:
Brand name: Gravel Ale
Volume: 300ml

```html
<!DOCTYPE html>
<html lang="en">
<head>
<meta charset="utf-8">
<title>Gravel Ale – Flavour Labels</title>
<link rel="stylesheet" href="https://fonts.googleapis.com/css2?family=Aldrich&family=Great+Vibes&display=swap">
<style>
  :root {
    --page: #ffffff;
    --shield-deep: #062a6b;
    --shield-mid: #0a4fa8;
    --brand-blue: #005fbf;
    --rim-light: #d8dde3;
    --rim-dark: #3a3f46;
    --ribbon-light: #39b6f2;
    --ribbon-dark: #0a77c7;
    --title: #ece6bf;
    --volume: #1b1b1b;
    --small: #cfd8e6;
    --abv: #e9eef6;
    --script: #f3ef8f;
    --honey: #f7c916;
    --banana: #f2cf2a;
    --lager-art: #2f8fa8;
    --zero-art: #29b9d8;
  }
  html, body {
    margin: 0;
    padding: 0;
    width: 1200px;
    height: 1154px;
    overflow: hidden;
    background: var(--page);
  }
  .label-sheet { display: block; width: 1200px; height: 1154px; }
  .neck-rim { fill: var(--rim-dark); }
  .neck-face { fill: var(--brand-blue); }
  .neck-name { font-family: "Aldrich", sans-serif; font-size: 15px; fill: var(--title); }
  .shield-rim { fill: url(#rimShade); }
  .shield-face { fill: url(#faceShade); }
  .volume { font-family: "Aldrich", sans-serif; font-size: 15px; fill: var(--volume); }
  .brand-name { font-family: "Aldrich", sans-serif; font-size: 29px; fill: var(--title); }
  .protein-tag { font-family: "Aldrich", sans-serif; font-size: 6px; fill: var(--small); }
  .abv { font-family: "Aldrich", sans-serif; font-size: 8px; fill: var(--abv); }
  .ribbon-tail { fill: var(--ribbon-dark); }
  .ribbon-band { fill: url(#ribbonShade); }
  .flavour-name { font-family: "Great Vibes", cursive; font-size: 21px; fill: var(--script); }
  .art-lager { fill: var(--lager-art); opacity: .7; }
  .art-honey { fill: var(--honey); }
  .art-banana { fill: var(--banana); }
  .art-zero { fill: var(--zero-art); }
</style>
</head>
<body>
<svg class="label-sheet" viewBox="0 0 1200 1154" xmlns="http://www.w3.org/2000/svg">
  <defs>
    <linearGradient id="rimShade" x1="0" y1="0" x2="1" y2="1">
      <stop offset="0" stop-color="var(--rim-light)"/>
      <stop offset=".5" stop-color="var(--rim-dark)"/>
      <stop offset="1" stop-color="var(--rim-light)"/>
    </linearGradient>
    <linearGradient id="faceShade" x1="0" y1="0" x2="0" y2="1">
      <stop offset="0" stop-color="var(--shield-mid)"/>
      <stop offset="1" stop-color="var(--shield-deep)"/>
    </linearGradient>
    <linearGradient id="ribbonShade" x1="0" y1="0" x2="0" y2="1">
      <stop offset="0" stop-color="var(--ribbon-light)"/>
      <stop offset="1" stop-color="var(--ribbon-dark)"/>
    </linearGradient>
    <g id="shield">
      <path class="shield-rim" d="M-107,8 Q-60,-6 -14,0 L0,9 L14,0 Q60,-6 107,8 L102,125 Q96,195 0,278 Q-96,195 -102,125 Z"/>
      <path class="shield-face" d="M-96,17 Q-55,6 -12,10 L0,17 L12,10 Q55,6 96,17 L92,124 Q86,185 0,262 Q-86,185 -92,124 Z"/>
      <text class="volume" x="0" y="48" text-anchor="middle">300 ml</text>
      <text class="brand-name" x="0" y="82" text-anchor="middle">Gravel Ale</text>
      <text class="protein-tag" x="-73" y="95">7g High Quality Protein</text>
    </g>
    <g id="ribbon">
      <path class="ribbon-tail" d="M-112,216 L-80,208 L-80,244 L-112,252 L-100,234 Z"/>
      <path class="ribbon-tail" d="M112,216 L80,208 L80,244 L112,252 L100,234 Z"/>
      <path class="ribbon-band" d="M-88,200 Q0,186 88,200 L88,236 Q0,222 -88,236 Z"/>
    </g>
    <g id="neck">
      <ellipse class="neck-rim" cx="0" cy="0" rx="64" ry="30"/>
      <ellipse class="neck-face" cx="0" cy="0" rx="57" ry="24"/>
      <text class="neck-name" x="0" y="5" text-anchor="middle">Gravel Ale</text>
    </g>
  </defs>

  <g class="label label-lager">
    <use href="#neck" x="155" y="317"/>
    <g transform="translate(160,575)">
      <use href="#shield"/>
      <rect class="art-lager" role="img" aria-label="Upward arrow artwork for the lager" x="-32" y="100" width="86" height="78" rx="6"/>
      <use href="#ribbon"/>
      <text class="abv" x="-68" y="184">Vol. 4%</text>
      <text class="flavour-name" x="0" y="229" text-anchor="middle">Larger</text>
    </g>
  </g>

  <g class="label label-honey">
    <use href="#neck" x="447" y="317"/>
    <g transform="translate(452,575)">
      <use href="#shield"/>
      <rect class="art-honey" role="img" aria-label="Honeycomb artwork for the honey ale" x="-40" y="100" width="82" height="88" rx="10"/>
      <use href="#ribbon"/>
      <text class="abv" x="-76" y="186">Vol. 4%</text>
      <text class="flavour-name" x="0" y="229" text-anchor="middle">Honey Ale</text>
    </g>
  </g>

  <g class="label label-banana">
    <use href="#neck" x="737" y="317"/>
    <g transform="translate(742,575)">
      <use href="#shield"/>
      <rect class="art-banana" role="img" aria-label="Banana bunch artwork for the banana ale" x="-75" y="106" width="135" height="62" rx="12"/>
      <use href="#ribbon"/>
      <text class="abv" x="-12" y="182">Vol. 4%</text>
      <text class="flavour-name" x="0" y="229" text-anchor="middle">Banana Ale</text>
    </g>
  </g>

  <g class="label label-zero">
    <use href="#neck" x="1030" y="317"/>
    <g transform="translate(1035,575)">
      <use href="#shield"/>
      <ellipse class="art-zero" role="img" aria-label="Glowing zero ring artwork for the alcohol-free beer" cx="4" cy="140" rx="38" ry="42"/>
      <use href="#ribbon"/>
      <text class="abv" x="-68" y="188">Vol. 0%</text>
      <text class="flavour-name" x="0" y="229" text-anchor="middle">Zero</text>
    </g>
  </g>
</svg>
</body>
</html>
```